Social Media designs (LinkedIn banner, LinkedIn posts, Instagram)

Hello designers!
We are looking to create some more concepts for our social media identity for a search firm (recruitment company)
I have attached a "brand toolkit" that shows our brand, logo, colour scheme to guide you with regards to colours and identiy.

You will see in the brand toolkit there are some examples of;
- A LinkedIn banner for the company (page 23)
- Social Media posts for LinkedIn and Instagram (page 21)

What we are looking for...

We don't really like the current LinkedIn banner ideas. We would like to see more concepts that look more aesthetically pleasing - the current ideas look quite dull.

We DO like the social media post concepts but we would like to have more templates/options that we can use (similar themes)

We welcome submissions for Social Media designs that we can use with our company branding. Thank you for your work in advance!

```html
<!DOCTYPE html>
<html lang="en">
<head>
<meta charset="utf-8">
<title>Harlow Reid — Social Media Set</title>
<link rel="stylesheet" href="https://fonts.googleapis.com/css2?family=Montserrat:wght@400;500;600;700;800&display=swap">
<style>
:root{
  --ink:#183229;
  --ink-deep:#122820;
  --green:#4a8a6e;
  --green-text:#5ea382;
  --sand:#cbc9c0;
  --sand-light:#d6d4cc;
  --paper:#ecebe6;
  --light:#efede6;
  --photo-a:#6f7c76;
  --photo-b:#a8aca4;
}
*{box-sizing:border-box;margin:0;padding:0}
html,body{width:1200px;height:2544px;overflow:hidden}
body{background:var(--paper);font-family:"Montserrat",sans-serif;position:relative;color:var(--light)}
.abs{position:absolute}
.masthead{position:absolute;left:0;top:0;width:1200px;height:140px;background:var(--ink);display:flex;align-items:center;justify-content:center;gap:18px}
.masthead .mark{width:46px;height:46px;background:var(--green)}
.masthead .name{font-size:40px;font-weight:600;line-height:1;color:var(--green)}
.brand{position:absolute;display:flex;align-items:center;gap:10px}
.brand .mark{width:26px;height:26px;background:var(--green)}
.brand .name{font-weight:600;font-size:17px;line-height:1.05;color:var(--light)}
.brand.on-sand .name{color:var(--ink)}
.photo{position:absolute;background:linear-gradient(160deg,var(--photo-b),var(--photo-a))}
.photo.round{border-radius:50%;border:6px solid var(--light)}
.plus{position:absolute;font-size:26px;font-weight:400;color:var(--light);line-height:1}
.url{position:absolute;font-size:9px;font-weight:500;color:var(--light)}
.lorem{position:absolute;font-size:8.5px;line-height:1.3;color:var(--light)}
/* banner */
.banner{position:absolute;left:60px;top:190px;width:1080px;height:270px;background:var(--ink);overflow:hidden}
.banner .sand{position:absolute;left:560px;top:0;width:165px;height:270px;background:var(--sand)}
.banner .panel{position:absolute;left:725px;top:0;width:355px;height:270px;background:var(--sand-light)}
.banner .we{position:absolute;left:38px;top:92px;font-weight:800;font-size:50px;color:var(--green-text);line-height:1}
.banner .we small{font-size:17px;font-weight:600;color:var(--light);margin-left:6px}
.banner .business{position:absolute;left:36px;top:138px;font-weight:800;font-size:60px;color:var(--light);line-height:1}
.banner .solution{position:absolute;left:38px;top:208px;font-weight:700;font-size:29px;letter-spacing:4px;color:var(--green-text)}
.banner .q1{position:absolute;left:760px;top:24px;font-size:28px;color:var(--green);font-weight:400}
.banner .q2{position:absolute;left:760px;top:58px;font-size:42px;color:var(--ink);font-weight:800;letter-spacing:1px}
.banner .rules{position:absolute;left:760px;top:108px;display:flex;gap:10px}
.banner .rules i{display:block;height:4px;background:var(--ink)}
.banner ul{position:absolute;left:760px;top:130px;list-style:none;font-size:13.5px;color:var(--green);line-height:1.3}
.banner li{position:relative;padding-left:22px;margin-bottom:10px}
.banner li::before{content:"";position:absolute;left:0;top:6px;width:6px;height:6px;background:var(--ink)}
/* posts */
.post{position:absolute;width:540px;height:540px;background:var(--ink);overflow:hidden}
.title{position:absolute;font-weight:800;line-height:1.05;color:var(--green-text)}
.sub{position:absolute;font-weight:500;color:var(--light)}
.card{position:absolute;background:var(--green);padding:20px 18px}
.card .t{font-weight:800;font-size:27px;line-height:1.05;color:var(--ink)}
.card .s{font-size:15px;line-height:1.2;color:var(--light);margin-top:12px}
.card .l{font-size:8px;line-height:1.3;color:var(--light);margin-top:12px}
.heavy{position:absolute;font-weight:800;color:var(--light);line-height:1.15}
</style>
</head>
<body>

<header class="masthead">
  <span class="mark"></span><span class="name">Harlow<br>Reid</span>
</header>

<section class="banner" aria-label="LinkedIn banner">
  <div class="sand"></div>
  <div class="panel"></div>
  <div class="photo" style="left:360px;top:0;width:230px;height:270px;background:linear-gradient(180deg,#58665f,#2e3d36)" role="img" aria-label="Businessman in a suit holding a notebook and pen"></div>
  <div class="brand" style="left:32px;top:26px"><span class="mark"></span><span class="name">Harlow<br>Reid</span></div>
  <span class="plus" style="left:290px;top:90px">+</span>
  <span class="plus" style="left:570px;top:58px">+</span>
  <span class="plus" style="left:690px;top:70px">+</span>
  <span class="plus" style="left:685px;top:198px">+</span>
  <span class="plus" style="left:520px;top:232px">+</span>
  <div class="we">WE<small>PROVIDE THE BEST</small></div>
  <div class="business">BUSINESS</div>
  <div class="solution">SOLUTION</div>
  <svg class="abs" style="left:300px;top:218px" width="52" height="26" viewBox="0 0 52 26" fill="none" stroke="#efede6" stroke-width="3"><polyline points="2,2 13,13 2,24"/><polyline points="18,2 29,13 18,24"/><polyline points="34,2 45,13 34,24"/></svg>
  <svg class="abs" style="left:600px;top:20px" width="40" height="20" viewBox="0 0 52 26" fill="none" stroke="#efede6" stroke-width="3"><polyline points="2,2 13,13 2,24"/><polyline points="18,2 29,13 18,24"/><polyline points="34,2 45,13 34,24"/></svg>
  <div class="q1">WHAT's OUR</div>
  <div class="q2">SERVICE?</div>
  <div class="rules"><i style="width:58px"></i><i style="width:70px"></i><i style="width:50px"></i></div>
  <ul>
    <li>Lorem ipsum dolor sit amet,<br>consectetuer adipiscing elit.</li>
    <li>Aliquam tincidunt mauris eu risus.</li>
    <li>Vestibulum auctor dapibus neque.</li>
    <li>Nunc dignissim risus id metus.</li>
  </ul>
</section>

<!-- post: resume -->
<article class="post" style="left:40px;top:580px">
  <div class="brand" style="left:28px;top:28px"><span class="mark"></span><span class="name">Harlow<br>Reid</span></div>
  <div class="title" style="right:32px;top:34px;font-size:30px;text-align:right">Make A<br>Resume Online</div>
  <div class="sub" style="right:32px;top:112px;font-size:16px">Win Over Employers</div>
  <p class="lorem" style="right:32px;top:140px;width:300px;text-align:right">Lorem ipsum is simply dummy text of the printing and typesetting industry, used as standard filler since the 1500s.</p>
  <span class="plus" style="left:80px;top:128px">+</span>
  <div class="abs" style="left:195px;top:195px;width:95px;height:28px;background:var(--sand)"></div>
  <div class="photo" style="left:34px;top:222px;width:285px;height:280px" role="img" aria-label="Team of colleagues working together at a laptop"></div>
  <div class="abs" style="left:360px;top:300px;width:180px;height:240px;background:var(--sand)"></div>
  <div class="abs" style="left:420px;top:380px;width:120px;height:90px;background:var(--ink)"></div>
  <span class="url" style="left:40px;bottom:14px">www.harlowreid.com</span>
</article>

<!-- post: market headshot -->
<article class="post" style="left:620px;top:580px">
  <div class="abs" style="left:0;top:0;width:540px;height:225px;background:var(--sand)"></div>
  <div class="abs" style="left:400px;top:0;width:140px;height:225px;background:var(--ink)"></div>
  <div class="abs" style="left:0;top:225px;width:540px;height:315px;background:linear-gradient(180deg,#2a4037,#152b22)" role="img" aria-label="Business handshake in an office"></div>
  <div class="brand on-sand" style="left:28px;top:28px"><span class="mark"></span><span class="name">Harlow<br>Reid</span></div>
  <svg class="abs" style="left:265px;top:95px" width="52" height="26" viewBox="0 0 52 26" fill="none" stroke="#183229" stroke-width="3"><polyline points="2,2 13,13 2,24"/><polyline points="18,2 29,13 18,24"/><polyline points="34,2 45,13 34,24"/></svg>
  <div class="card" style="left:32px;top:118px;width:195px;height:265px">
    <div class="t">Make A<br>Business</div>
    <div class="s">Win Over<br>Employers</div>
    <div class="l">Lorem ipsum is simply dummy text of the printing and typesetting industry, used as standard filler since the 1500s.</div>
  </div>
  <div class="photo round" style="left:305px;top:125px;width:225px;height:225px" role="img" aria-label="Portrait of a businessman in glasses"></div>
  <div class="heavy" style="right:28px;bottom:42px;font-size:24px;text-align:right">THE BEST IN<br>THE MARKET</div>
  <span class="url" style="left:0;right:0;bottom:12px;text-align:center">www.harlowreid.com</span>
</article>

<!-- post: business team -->
<article class="post" style="left:40px;top:1220px">
  <div class="abs" style="left:0;top:0;width:345px;height:540px;background:var(--sand)"></div>
  <div class="brand on-sand" style="left:28px;top:28px"><span class="mark"></span><span class="name">Harlow<br>Reid</span></div>
  <svg class="abs" style="left:255px;top:88px" width="52" height="26" viewBox="0 0 52 26" fill="none" stroke="#4a8a6e" stroke-width="3"><polyline points="2,2 13,13 2,24"/><polyline points="18,2 29,13 18,24"/><polyline points="34,2 45,13 34,24"/></svg>
  <div class="photo" style="left:0;top:155px;width:345px;height:385px" role="img" aria-label="Colleagues smiling during an office meeting"></div>
  <div class="title" style="right:28px;top:30px;font-size:28px;text-align:right">Make A<br>Business</div>
  <div class="sub" style="right:28px;top:100px;font-size:15px;text-align:right">Win Over<br>Employers</div>
  <p class="lorem" style="right:28px;top:150px;width:150px;text-align:center">Lorem ipsum is simply dummy text of the printing and typesetting industry, used as standard filler since the 1500s.</p>
  <div class="photo round" style="left:288px;top:268px;width:225px;height:225px" role="img" aria-label="Portrait of a businessman leaning on a desk"></div>
  <span class="url" style="left:40px;bottom:14px">www.harlowreid.com</span>
</article>

<!-- post: best in the market -->
<article class="post" style="left:620px;top:1220px">
  <div class="brand" style="left:28px;top:28px"><span class="mark"></span><span class="name">Harlow<br>Reid</span></div>
  <div class="heavy" style="right:28px;top:30px;font-size:18px;text-align:right">THE BEST IN<br>THE MARKET</div>
  <div class="abs" style="left:420px;top:330px;width:120px;height:210px;background:var(--sand)"></div>
  <div class="abs" style="left:470px;top:400px;width:70px;height:80px;background:var(--ink)"></div>
  <div class="photo" style="left:0;top:85px;width:340px;height:410px" role="img" aria-label="Business partners shaking hands at a meeting table"></div>
  <div class="card" style="left:290px;top:125px;width:190px;height:260px">
    <div class="t">Make A<br>Business</div>
    <div class="s">Win Over<br>Employers</div>
    <div class="l">Lorem ipsum is simply dummy text of the printing and typesetting industry, used as standard filler since the 1500s.</div>
  </div>
  <span class="url" style="left:28px;bottom:12px">www.harlowreid.com</span>
</article>

<!-- post: best company -->
<article class="post" style="left:40px;top:1860px">
  <div class="brand" style="left:28px;top:28px"><span class="mark"></span><span class="name">Harlow<br>Reid</span></div>
  <div class="title" style="left:38px;top:100px;font-size:42px"><span style="color:var(--sand)">Make A</span><br>Business</div>
  <div class="abs" style="left:505px;top:15px;width:28px;height:28px;background:var(--green)"></div>
  <div class="photo" style="left:330px;top:30px;width:175px;height:170px" role="img" aria-label="Man in a dark turtleneck and blazer"></div>
  <div class="abs" style="left:330px;top:215px;width:190px;height:1px;background:var(--light);opacity:.5"></div>
  <div class="abs" style="left:230px;top:290px;width:120px;height:250px;background:var(--green)"></div>
  <div class="photo" style="left:0;top:250px;width:300px;height:290px" role="img" aria-label="Businessman in glasses holding a notebook and pen"></div>
  <div class="heavy" style="right:28px;top:255px;font-size:28px;font-weight:600;text-align:right">THE<br>BEST<br>COMPANY</div>
  <div class="abs" style="left:330px;top:385px;width:190px;height:1px;background:var(--light);opacity:.5"></div>
  <p class="lorem" style="right:30px;top:395px;width:170px;text-align:center;letter-spacing:.5px">Lorem ipsum dolor sit amet, consectetuer adipiscing elit, sed diam nonummy.</p>
  <span class="url" style="right:28px;bottom:14px">www.harlowreid.com</span>
</article>

<!-- post: win over employers -->
<article class="post" style="left:620px;top:1860px">
  <div class="abs" style="left:0;top:140px;width:540px;height:350px;background:var(--sand)"></div>
  <div class="brand" style="left:28px;top:38px"><span class="mark"></span><span class="name">Harlow<br>Reid</span></div>
  <div class="photo" style="left:250px;top:25px;width:250px;height:420px" role="img" aria-label="Businessmen shaking hands in a bright office"></div>
  <div class="abs" style="left:238px;top:150px;width:3px;height:110px;background:var(--green)"></div>
  <div class="abs" style="left:510px;top:300px;width:3px;height:230px;background:var(--green)"></div>
  <div class="title" style="left:32px;top:160px;font-size:34px">Make A<br>Business</div>
  <div class="sub" style="left:32px;top:245px;font-size:17px;color:var(--ink)">Win Over<br>Employers</div>
  <p class="lorem" style="left:32px;top:300px;width:200px;color:var(--ink)">Lorem ipsum is simply dummy text of the printing and typesetting industry, used as standard filler since the 1500s.</p>
  <span class="url" style="left:40px;bottom:20px">www.harlowreid.com</span>
</article>

</body>
</html>
```